An anniversary gift for my girlfriend

My girlfriend and I have been dating for almost 2 years. We met online and this has afforded us the really unique opportunity to have the first words we said to each other (the whole conversation, in fact) preserved. We're moving in together in a few months and she doesn't know that I saved the conversation. I've been waiting for this to turn it into something we can hang in our new place.

The only phrase I want to use is:
"Well if you dislike people's knees then I think we'll get along famously"

It's an Nobody Leaves Before Midnight in Portland reference for the curious.

I want the poster to use the words themselves as the art; I'm thinking typography. I'd like it to match her aesthetic, she likes to wear Nora Vell and T. Brisk. Colors shouldn't be anything too "girly". Somewhere I'd like to include the date June 1, 2015. It shouldn't be a major piece of the poster though, just a way to denote the date.

It should fit (and be fully visible in) a 16x20 (inches) frame

Thanks in advance for the work!

Requirements
Must have
• Must use only the words: "Well if you dislike people's knees then I think we'll get along famously"
• I want this to be typography, so making the phrase the center of the poster and the art itself.

```html
<!DOCTYPE html>
<html lang="en">
<head>
<meta charset="utf-8">
<title>Well if you dislike people's knees</title>
<link rel="stylesheet" href="https://fonts.googleapis.com/css2?family=Questrial&family=Oswald:wght@400&display=swap">
<style>
  :root {
    --ink-cream: #f4f1c6;
    --date-rose: #c2255c;
    --bg-dark: #151515;
    --bg-deep: #080808;
    --bg-blue: #0d1a24;
  }
  html, body {
    margin: 0;
    padding: 0;
    width: 960px;
    height: 1200px;
    overflow: hidden;
    background: var(--bg-deep);
  }
  .poster {
    position: relative;
    width: 960px;
    height: 1200px;
    overflow: hidden;
  }
  .keyboard-backdrop {
    position: absolute;
    inset: 0;
    background:
      radial-gradient(ellipse at 92% 55%, var(--bg-blue) 0%, transparent 22%),
      radial-gradient(ellipse at 45% 45%, #222 0%, var(--bg-dark) 45%, var(--bg-deep) 100%);
  }
  .phrase {
    position: absolute;
    inset: 0;
  }
  .word {
    font-family: "Questrial", "Century Gothic", sans-serif;
    fill: var(--ink-cream);
  }
  .rule {
    fill: var(--ink-cream);
  }
  .date {
    font-family: "Oswald", "Arial Narrow", sans-serif;
    fill: var(--date-rose);
  }
</style>
</head>
<body>
<main class="poster">
  <div class="keyboard-backdrop" role="img" aria-label="Dark, softly lit close-up photograph of computer keyboard keys"></div>

  <svg class="phrase" width="960" height="1200" viewBox="0 0 960 1200" aria-label="Well if you dislike people's knees then I think we'll get along famously">
    <!-- vertical rules -->
    <rect class="rule" x="437" y="0" width="6" height="262"/>
    <rect class="rule" x="285" y="280" width="6" height="126"/>
    <rect class="rule" x="604" y="410" width="6" height="56"/>
    <rect class="rule" x="518" y="482" width="6" height="170"/>
    <rect class="rule" x="601" y="470" width="6" height="730"/>

    <!-- phrase -->
    <text class="word" x="312" y="188" font-size="74" textLength="150" lengthAdjust="spacingAndGlyphs">well</text>
    <text class="word" x="215" y="274" font-size="100" textLength="275" lengthAdjust="spacingAndGlyphs">if you</text>
    <text class="word" x="318" y="343" font-size="68" textLength="212" lengthAdjust="spacingAndGlyphs">dislike</text>
    <text class="word" x="318" y="396" font-size="68" textLength="307" lengthAdjust="spacingAndGlyphs">people's</text>
    <text class="word" font-size="68" textLength="165" lengthAdjust="spacingAndGlyphs" transform="translate(698,400) rotate(-90)">knees</text>
    <text class="word" x="226" y="505" font-size="136" textLength="282" lengthAdjust="spacingAndGlyphs">then</text>
    <text class="word" font-size="60" textLength="140" lengthAdjust="spacingAndGlyphs" transform="translate(288,655) rotate(-90)">think</text>
    <text class="word" x="318" y="584" font-size="68" textLength="174" lengthAdjust="spacingAndGlyphs">we'll</text>
    <text class="word" x="358" y="636" font-size="68" textLength="134" lengthAdjust="spacingAndGlyphs">get</text>
    <text class="word" x="318" y="754" font-size="146" textLength="390" lengthAdjust="spacingAndGlyphs">along</text>
    <text class="word" y="834" font-size="76"><tspan x="298" textLength="287" lengthAdjust="spacingAndGlyphs">famous</tspan><tspan x="598">l</tspan><tspan x="614" textLength="52" lengthAdjust="spacingAndGlyphs">y</tspan></text>

    <!-- date -->
    <text class="date" font-size="50" textLength="230" lengthAdjust="spacingAndGlyphs" transform="translate(598,1160) rotate(-90)">6.01.2015</text>
  </svg>
</main>
</body>
</html>
```